Re-brand our business and design!

We need a simple informational website (editable for in the future use)
We need our logo(we have included logo), name, who we are, and what we do displayed.

This is our current site (which is not acceptable, and only a template site): all our information is on this site, please use it forreferanceofinformation.
Www.brightlanefixers.com

Target Market(s)

Real estate brokers, and realtors,homeowners, and anyone looking for home repairs.

Industry/Entity Type

Business

Number of Pages Required

4 page

Font styles to use
Sans Serif

Requirements
Must have
• Our name, contact info, services, and our logo (which we will Email upon request)
• MUST have originality to the site.
• custom "contact us form" or request an estimate form.
Nice to have
• page for real customer testimonies.
• page for our previous work where we can upload pics of completed jobs.
Should not have
• any infringements on any copyrights or plagiarism at all.

```html
<!DOCTYPE html>
<html lang="en">
<head>
<meta charset="UTF-8">
<title>Brightlane Fixers – Home Repairs and Maintenance</title>
<link href="https://fonts.googleapis.com/css2?family=Open+Sans:ital,wght@0,300;0,400;0,600;0,700;1,300;1,400;1,700&display=swap" rel="stylesheet">
<style>
  :root{
    --white:#ffffff;
    --page:#ffffff;
    --section-grey:#e9e9e9;
    --text-dark:#3f3f3f;
    --text-body:#4a4a4a;
    --brand-red:#dc0b0b;
    --card-white:#ffffff;
    --hero-dark:#2e3a2c;
  }
  *{box-sizing:border-box;margin:0;padding:0}
  html,body{width:1200px;height:1200px;overflow:hidden;background:var(--page)}
  body{font-family:'Open Sans',sans-serif;position:relative}

  .site{position:absolute;left:79px;top:74px;width:1040px;height:1126px;overflow:hidden;background:var(--section-grey)}

  .hero{position:absolute;left:0;top:0;width:1040px;height:636px;overflow:hidden}
  .hero-photo{position:absolute;inset:0;
    background:
      radial-gradient(ellipse 40% 30% at 55% 40%, rgba(190,195,195,.45), transparent 70%),
      linear-gradient(180deg,#4a4d48 0%,#5d625a 30%,#4c6a3e 62%,#3f7a2e 78%,#2f4d22 100%);}
  .hero-shade{position:absolute;inset:0;background:rgba(20,25,20,.35)}

  .brand{position:absolute;top:52px;left:0;width:1040px;display:flex;justify-content:center;align-items:center;gap:10px;color:var(--white);font-weight:700;font-size:16px}
  .brand-mark{width:14px;height:14px;background:var(--white)}

  .main-nav{position:absolute;top:214px;left:0;width:1040px;display:flex;justify-content:center;gap:38px}
  .main-nav a{color:var(--white);text-decoration:none;font-weight:700;font-size:12px;letter-spacing:.2px}

  .hero-title{position:absolute;top:346px;left:0;width:1040px;text-align:center;color:var(--white);font-weight:300;font-style:italic;font-size:54px;line-height:68px}

  .contact-item{position:absolute;top:512px;display:flex;align-items:center;gap:14px;color:var(--white)}
  .contact-item.phone{left:243px}
  .contact-item.email{left:472px}
  .contact-icon{width:33px;height:33px;border:1px solid rgba(255,255,255,.7);border-radius:50%;display:flex;align-items:center;justify-content:center}
  .contact-label{font-size:10px;text-transform:uppercase;letter-spacing:.3px;line-height:12px}
  .contact-value{font-size:19px;font-weight:700;line-height:24px}

  .intro{position:absolute;top:636px;left:0;width:1040px;height:490px;
    background:linear-gradient(180deg,var(--section-grey) 0%,var(--section-grey) 48%,#f0f0f0 75%,#f6f6f6 100%)}
  .tagline{position:absolute;top:138px;left:0;width:1040px;text-align:center;font-style:italic;font-weight:700;font-size:19px;line-height:29px;color:var(--text-dark)}
  .intro-text{position:absolute;top:206px;left:90px;width:860px;text-align:center;font-size:14.4px;line-height:24px;color:var(--text-body)}

  .service-card{position:absolute;width:170px;height:222px;background:var(--card-white);box-shadow:0 1px 3px rgba(0,0,0,.15);display:flex;flex-direction:column;align-items:center;color:var(--text-dark)}
  .service-card svg{margin-top:55px}
  .service-card h3{margin-top:auto;margin-bottom:48px;font-size:14px;font-weight:600;text-transform:uppercase;text-align:center;line-height:18px}
  .service-card.active{background:var(--brand-red);color:var(--white);box-shadow:0 4px 22px rgba(220,11,11,.45)}
  .service-card.active h3{margin-bottom:30px}
  .card-1{left:223px;top:286px}
  .card-2{left:435px;top:286px}
  .card-3{left:646px;top:286px}
  .card-4{left:223px;top:549px}
  .card-5{left:435px;top:549px}
  .card-6{left:646px;top:549px}
</style>
</head>
<body>
<div class="site">
  <header class="hero">
    <div class="hero-photo" role="img" aria-label="Photo of a modern two-storey house with a green lawn, stepping stones and tropical palms"></div>
    <div class="hero-shade"></div>
    <div class="brand"><span class="brand-mark"></span>Brightlane Fixers</div>
    <nav class="main-nav">
      <a href="#">HOME</a>
      <a href="#">ABOUT US</a>
      <a href="#">TESTIMONIALS</a>
      <a href="#">CONTACT US</a>
    </nav>
    <h1 class="hero-title">Brightlane Fixers<br>And Maintenance</h1>
    <div class="contact-item phone">
      <span class="contact-icon">
        <svg width="14" height="14" viewBox="0 0 24 24" fill="#fff"><path d="M6.6 10.8a15.1 15.1 0 0 0 6.6 6.6l2.2-2.2a1 1 0 0 1 1-.25 11.4 11.4 0 0 0 3.6.57 1 1 0 0 1 1 1V20a1 1 0 0 1-1 1A17 17 0 0 1 3 4a1 1 0 0 1 1-1h3.5a1 1 0 0 1 1 1c0 1.25.2 2.45.57 3.57a1 1 0 0 1-.25 1z"/></svg>
      </span>
      <div><div class="contact-label">Call us</div><div class="contact-value">812-555-0147</div></div>
    </div>
    <div class="contact-item email">
      <span class="contact-icon">
        <svg width="15" height="12" viewBox="0 0 24 18" fill="none" stroke="#fff" stroke-width="2"><rect x="1" y="1" width="22" height="16"/><path d="M1 1l11 9 11-9"/></svg>
      </span>
      <div><div class="contact-label">Any inquiry email us</div><div class="contact-value">Mark@brightlanefixers.com</div></div>
    </div>
  </header>

  <section class="intro">
    <p class="tagline">One Name, One number, One call means one service for fast timely quotes,<br>home repairs and updates for you and/or your clients.</p>
    <p class="intro-text">Looking for someone to help get your listing ready to show? A complete Home Repair Solution? Did an inspection reveal repairs needed before closing? Brightlane Fixers can help!</p>

    <div class="service-card card-1">
      <svg width="74" height="66" viewBox="0 0 74 66" fill="none" stroke="#dc0b0b" stroke-width="2.2" stroke-linejoin="round">
        <path d="M4 60 L58 8 L70 20 L62 28 L12 64 Z"/>
        <path d="M56 14 L64 22 M52 16 L66 16"/>
        <path d="M8 62 l2 3 M14 58 l2 3 M20 54 l2 3 M26 50 l2 3 M32 46 l2 3 M38 42 l2 3"/>
      </svg>
      <h3>Carpentry</h3>
    </div>
    <div class="service-card card-2 active">
      <svg width="54" height="82" viewBox="0 0 54 82" fill="none" stroke="#fff" stroke-width="2.2">
        <path d="M20 2 L2 80 M28 2 L10 80 M20 2 L28 2"/>
        <path d="M28 2 L52 80 M32 20 L44 80"/>
        <path d="M16 20 L30 20 M12 36 L36 36 M9 52 L40 52 M6 68 L46 68"/>
      </svg>
      <h3>Small<br>Construction</h3>
    </div>
    <div class="service-card card-3">
      <svg width="74" height="74" viewBox="0 0 74 74" fill="none" stroke="#dc0b0b" stroke-width="2.2">
        <circle cx="56" cy="18" r="6"/>
        <path d="M52 10 L62 2 L70 10 L62 22"/>
        <path d="M50 22 C40 30 30 30 18 40 C6 50 6 66 16 70 C14 56 26 46 44 34"/>
        <path d="M48 28 C44 40 40 50 30 58 C22 66 24 72 34 70 C44 58 52 44 56 26"/>
      </svg>
      <h3>Electrical</h3>
    </div>
    <div class="service-card card-4"></div>
    <div class="service-card card-5"></div>
    <div class="service-card card-6"></div>
  </section>
</div>
</body>
</html>
```